ASSET BASED PROGRAM FLIER

Need flier to market hard money loan products offered HARD MONEY FIX & FLIP PROGRAMS

We offer a variety of loan programs Some program highlights include......

1) No Minimum Credit Score
2) 3-5 Day Close
3) Up to 100% of Purchase & Rehab
4) Rates as Low as 7%
5) Loans Offered Nationwide

Contact us today for more information at (800) 647-2915 x42 or email us at mwelton@brightlanefunding.example NMLS #731856 www.brightlanefunding.example

```html
<!DOCTYPE html>
<html lang="en">
<head>
<meta charset="utf-8">
<title>Hard Money Fix &amp; Flip Programs – Bright Lane Funding</title>
<link rel="stylesheet" href="https://fonts.googleapis.com/css2?family=Cinzel:wght@500;600&family=Tinos&family=Ubuntu:ital,wght@0,400;0,500;0,700;1,700&display=swap">
<style>
  :root {
    --page-bg: #e9e6e1;
    --paper: #ffffff;
    --brand-blue: #1560a8;
    --headline-blue: #1a5ea8;
    --olive: #b0a035;
    --olive-dark: #9e8f2c;
    --yellow: #f7ec00;
    --ink-gray: #4a4a4a;
    --bar-gray: #e3e3e4;
    --ink-dark: #1f1f1f;
    --white: #ffffff;
  }
  * { box-sizing: border-box; margin: 0; padding: 0; }
  html, body { width: 894px; height: 1200px; overflow: hidden; }
  body { background: var(--page-bg); font-family: "Ubuntu", sans-serif; }

  .flyer {
    position: absolute; left: 24px; top: 0;
    width: 846px; height: 1200px;
    background: var(--paper); overflow: hidden;
  }

  .brand {
    position: absolute; left: 40px; top: 88px;
    display: flex; align-items: center; gap: 12px;
  }
  .brand-dot { width: 34px; height: 34px; border-radius: 50%; background: var(--headline-blue); }
  .brand-name { font-weight: 500; font-size: 28px; color: var(--headline-blue); }

  .headline {
    position: absolute; left: 372px; top: 86px;
    font-family: "Cinzel", serif; font-weight: 600; font-size: 45px; line-height: 52px;
    color: var(--headline-blue); letter-spacing: 0.5px;
  }

  .photo {
    position: absolute; left: 0; top: 228px; width: 846px; height: 552px;
    background: linear-gradient(170deg, #ffffff 0%, #f1ede6 22%, #cbbfa8 50%, #a3927c 78%, #857868 100%);
  }

  .subhead {
    position: absolute; left: 46px; top: 272px;
    font-weight: 700; font-size: 32px; line-height: 45px; color: var(--ink-gray);
  }

  .web-band {
    position: absolute; left: 0; top: 718px; width: 846px; height: 60px;
    background: linear-gradient(90deg, var(--olive-dark) 0%, var(--olive) 45%, #d9cc1e 75%, var(--yellow) 100%);
  }
  .web-address {
    position: absolute; left: 46px; top: 728px;
    font-weight: 700; font-style: italic; font-size: 28px; letter-spacing: 1px; color: var(--white);
  }

  .programs {
    position: absolute; left: 0; top: 778px; width: 846px; height: 304px;
    background: var(--brand-blue); color: var(--white);
  }
  .programs-title { position: absolute; left: 46px; top: 22px; font-weight: 700; font-size: 30px; }
  .programs-intro { position: absolute; left: 46px; top: 66px; font-weight: 700; font-size: 21px; }
  .highlights {
    position: absolute; left: 46px; top: 112px; width: 760px;
    list-style: none; display: grid; grid-template-columns: 395px 1fr; row-gap: 9px;
    font-size: 21px; line-height: 30px;
  }
  .highlights li { display: flex; align-items: center; gap: 10px; }
  .highlights li svg { flex: none; }

  .contact-bar { position: absolute; left: 36px; top: 260px; width: 770px; height: 44px; }
  .contact-bar svg { position: absolute; inset: 0; }
  .contact-email, .contact-nmls {
    position: absolute; top: 10px; font-weight: 700; font-size: 20px; color: var(--ink-dark);
  }
  .contact-email { left: 26px; }
  .contact-nmls { right: 26px; }

  .badge {
    position: absolute; z-index: 2; left: 579px; top: 578px; width: 236px; height: 236px;
    border-radius: 50%; background: radial-gradient(circle at 50% 40%, #ffffff 55%, #e4e4e4 100%);
    border: 7px solid var(--yellow);
    box-shadow: 0 3px 8px rgba(0,0,0,0.25);
    display: flex; align-items: center; justify-content: center; text-align: center;
    font-weight: 700; font-size: 29px; line-height: 37px; color: var(--ink-dark);
  }

  .call-band {
    position: absolute; left: 0; top: 1082px; width: 846px; height: 118px;
    background: var(--olive); color: var(--white);
  }
  .call-lead { position: absolute; left: 46px; top: 20px; font-size: 27px; line-height: 33px; }
  .call-phone { position: absolute; left: 346px; top: 20px; font-family: "Tinos", serif; font-size: 52px; line-height: 60px; }
</style>
</head>
<body>
<main class="flyer">
  <div class="brand">
    <span class="brand-dot"></span>
    <span class="brand-name">Bright Lane Funding</span>
  </div>

  <h1 class="headline">HARD MONEY FIX<br>&amp; FLIP PROGRAMS</h1>

  <div class="photo" role="img" aria-label="Smiling construction worker in a yellow hard hat and plaid shirt carrying lumber on his shoulder, with a blurred yellow loader behind him"></div>

  <p class="subhead">Check Out Our Exciting<br>New Product Line</p>

  <div class="web-band"></div>
  <p class="web-address">www.brightlanefunding.example</p>

  <section class="programs">
    <h2 class="programs-title">We offer a variety of loan programs</h2>
    <p class="programs-intro">Some program highlights include......</p>
    <ul class="highlights">
      <li><svg width="18" height="18" viewBox="0 0 18 18"><circle cx="9" cy="9" r="9" fill="#e8d36a"/><path d="M4.5 9.2l3 3 6-6.4" fill="none" stroke="#1560a8" stroke-width="2.2"/></svg>No Minimum Credit Score</li>
      <li><svg width="18" height="18" viewBox="0 0 18 18"><circle cx="9" cy="9" r="9" fill="#e8d36a"/><path d="M4.5 9.2l3 3 6-6.4" fill="none" stroke="#1560a8" stroke-width="2.2"/></svg>3-5 Day Close</li>
      <li><svg width="18" height="18" viewBox="0 0 18 18"><circle cx="9" cy="9" r="9" fill="#e8d36a"/><path d="M4.5 9.2l3 3 6-6.4" fill="none" stroke="#1560a8" stroke-width="2.2"/></svg>Up to 100% of Purchase &amp; Rehab</li>
      <li><svg width="18" height="18" viewBox="0 0 18 18"><circle cx="9" cy="9" r="9" fill="#e8d36a"/><path d="M4.5 9.2l3 3 6-6.4" fill="none" stroke="#1560a8" stroke-width="2.2"/></svg>Rates as Low as 7%</li>
      <li><svg width="18" height="18" viewBox="0 0 18 18"><circle cx="9" cy="9" r="9" fill="#e8d36a"/><path d="M4.5 9.2l3 3 6-6.4" fill="none" stroke="#1560a8" stroke-width="2.2"/></svg>Loans Offered Nationwide</li>
    </ul>

    <div class="contact-bar">
      <svg width="770" height="44" viewBox="0 0 770 44"><path d="M10 0 H760 L770 44 H0 Z" fill="#e3e3e4"/></svg>
      <span class="contact-email">email us at mwelton@brightlanefunding.example</span>
      <span class="contact-nmls">NMLS #731856</span>
    </div>
  </section>

  <div class="badge">Hard<br>Money Loan<br>Products<br>offered</div>

  <section class="call-band">
    <p class="call-lead">Contact us today for<br>more information at</p>
    <p class="call-phone">(800) 647-2915 x42</p>
  </section>
</main>
</body>
</html>
```